An innovative software company needs a business card!

We need a business card design for our new innovative software company. Please use the details for the business card provided in business card details section. We will use the business card paper like: https://www.plavex.com/us/products/nfc/business-cards-plus.html Our company name: kelvora We have already a logo and colors to use in business cards too ,

Target Market(s)

App & Sofware Development

Industry/Entity Type

Software

Contact Information for Business Card

Lukas Brenner, BSc.
Owner and Creative Superhero

Adress:
Tulpenweg 37/4/1809
A - 1100, Wien

Tel: +43 (0) 676 921 35 60
Email: lukas.brenner@kelvora.at
Web: www.kelvora.at

Requirements
Must have
• - Use our logo
Nice to have
• It would be nice to have a nice picture on the backside. (About apps, software, technicals or funy stuff) - Use our colors as in business card (optional)

```html
<!DOCTYPE html>
<html lang="en">
<head>
<meta charset="utf-8">
<title>kelvora – Business Card</title>
<link href="https://fonts.googleapis.com/css2?family=Montserrat:wght@400;500;700;800&display=swap" rel="stylesheet">
<style>
  :root {
    --page-bg: #e9eaec;
    --card-black: #050505;
    --navy-deep: #05070f;
    --navy-mid: #0d1a2c;
    --brand-blue: #17a3d6;
    --light-grey: #c3c5c9;
    --white: #ffffff;
  }
  * { box-sizing: border-box; margin: 0; padding: 0; }
  html, body { width: 1200px; height: 900px; overflow: hidden; }
  body {
    background: var(--page-bg);
    font-family: "Montserrat", Arial, sans-serif;
    position: relative;
  }
  .card {
    position: absolute;
    left: 270px;
    width: 660px;
    height: 377px;
    border-radius: 22px;
    overflow: hidden;
    box-shadow: 0 10px 30px rgba(0,0,0,.25);
  }

  /* Back side */
  .card--back { top: 48px; background: var(--navy-deep); }
  .back-art {
    position: absolute; inset: 0;
    background:
      radial-gradient(ellipse 70% 22% at 62% 42%, rgba(60,120,150,.35), transparent 70%),
      linear-gradient(160deg, var(--navy-mid) 0%, var(--navy-deep) 70%);
  }
  .back-brand {
    position: absolute; left: 0; right: 0; top: 130px;
    display: flex; align-items: center; justify-content: center; gap: 16px;
  }
  .brand-dot {
    width: 46px; height: 46px; border-radius: 50%;
    background: var(--brand-blue);
  }
  .brand-name {
    color: var(--brand-blue);
    font-weight: 800;
    font-size: 64px;
    letter-spacing: 1px;
    line-height: 1;
  }
  .back-url {
    position: absolute; left: 0; right: 0; bottom: 62px;
    text-align: center;
    color: var(--brand-blue);
    font-size: 20px;
    letter-spacing: 1px;
  }
  .back-url strong { color: var(--white); font-weight: 700; }

  /* Front side */
  .card--front { top: 474px; background: var(--card-black); }
  .front-brand {
    position: absolute; left: 40px; top: 40px;
    display: flex; align-items: center; gap: 16px;
  }
  .front-brand .brand-dot { width: 54px; height: 54px; }
  .front-brand .brand-name { font-size: 70px; }

  .identity {
    position: absolute; right: 72px; top: 136px;
    text-align: right;
  }
  .identity__name {
    color: var(--brand-blue);
    font-size: 24px; font-weight: 500; letter-spacing: .5px;
  }
  .identity__title {
    color: var(--white);
    font-size: 14px; margin-top: 2px;
  }
  .accent-square {
    position: absolute; right: 0; top: 128px;
    width: 26px; height: 42px;
    background: var(--brand-blue);
  }
  .divider {
    position: absolute; left: 120px; right: 44px; top: 196px;
    height: 2px; background: var(--brand-blue);
  }
  .address {
    position: absolute; right: 44px; top: 212px;
    text-align: right;
    color: var(--white); font-size: 15px; line-height: 1.5;
  }
  .contacts {
    position: absolute; left: 120px; top: 212px;
    list-style: none;
    color: var(--white); font-size: 15px; line-height: 1.75;
  }
  .contacts li { display: flex; align-items: center; gap: 12px; }
  .contacts svg { width: 12px; height: 12px; fill: var(--brand-blue); flex: none; }
  .contacts .hl { color: var(--brand-blue); font-weight: 700; }

  .bottom-band {
    position: absolute; left: 0; right: 0; bottom: 0; height: 14px;
    display: flex;
  }
  .bottom-band__grey { width: 56%; background: var(--light-grey); }
  .bottom-band__blue { flex: 1; background: var(--brand-blue); }
  .right-edge {
    position: absolute; right: 0; bottom: 14px;
    width: 8px; height: 42px; background: var(--brand-blue);
  }
</style>
</head>
<body>

  <section class="card card--back" aria-label="Business card back">
    <div class="back-art" role="img" aria-label="Dark navy background with soft light streaks"></div>
    <div class="back-brand">
      <span class="brand-dot"></span>
      <span class="brand-name">kelvora</span>
    </div>
    <p class="back-url">www.<strong>kelvora</strong>.at</p>
  </section>

  <section class="card card--front" aria-label="Business card front">
    <div class="front-brand">
      <span class="brand-dot"></span>
      <span class="brand-name">kelvora</span>
    </div>

    <span class="accent-square"></span>
    <div class="identity">
      <p class="identity__name">Lukas Brenner, BSc</p>
      <p class="identity__title">Owner and Creative Superhero</p>
    </div>

    <div class="divider"></div>

    <ul class="contacts">
      <li>
        <svg viewBox="0 0 24 24" aria-hidden="true"><path d="M6.6 10.8a15 15 0 0 0 6.6 6.6l2.2-2.2c.3-.3.7-.4 1-.2 1.1.4 2.3.6 3.6.6.6 0 1 .4 1 1V20c0 .6-.4 1-1 1A17 17 0 0 1 3 4c0-.6.4-1 1-1h3.5c.6 0 1 .4 1 1 0 1.3.2 2.5.6 3.6.1.3 0 .7-.2 1z"/></svg>
        +43 (0) 676 921 35 60
      </li>
      <li>
        <svg viewBox="0 0 24 24" aria-hidden="true"><path d="M12 2a10 10 0 1 0 0 20 10 10 0 0 0 0-20zm6.9 6h-3a15 15 0 0 0-1.3-3.6A8 8 0 0 1 18.9 8zM12 4c.8 1.2 1.5 2.5 1.9 4h-3.8c.4-1.5 1.1-2.8 1.9-4zM4.3 14a8 8 0 0 1 0-4h3.4a16 16 0 0 0 0 4zm.8 2h3a15 15 0 0 0 1.3 3.6A8 8 0 0 1 5.1 16zm3-8h-3a8 8 0 0 1 4.3-3.6C8.8 5.6 8.4 6.8 8.1 8zM12 20c-.8-1.2-1.5-2.5-1.9-4h3.8c-.4 1.5-1.1 2.8-1.9 4zm2.3-6H9.7a14 14 0 0 1 0-4h4.6a14 14 0 0 1 0 4zm.3 5.6c.6-1.1 1-2.3 1.3-3.6h3a8 8 0 0 1-4.3 3.6zm1.7-5.6a16 16 0 0 0 0-4h3.4a8 8 0 0 1 0 4z"/></svg>
        <span>www.<span class="hl">kelvora</span>.at</span>
      </li>
      <li>
        <svg viewBox="0 0 24 24" aria-hidden="true"><path d="M3 5h18v14H3zm2 2v.5l7 4.5 7-4.5V7zm0 2.9V17h14V9.9l-7 4.5z"/></svg>
        lukas.brenner@kelvora.at
      </li>
    </ul>

    <address class="address" style="font-style:normal">
      Tulpenweg 37/4/1809<br>
      A - 1100, Wien
    </address>

    <span class="right-edge"></span>
    <div class="bottom-band">
      <span class="bottom-band__grey"></span>
      <span class="bottom-band__blue"></span>
    </div>
  </section>

</body>
</html>
```